Psychology and Counselling Relationship Centre wants a Website

We need a SEO Website that is professional and simple Company Logo and colours is done and supplied

Target Market(s)

People wanting marriage Counselling / Parenting Issues / Relationship issues

Industry/Entity Type

Psychology

Coding

Coded - Design and coding required

Number of Pages Required

5+ page

Font styles to use
Other font styles liked:
• calibri

Colors
32a6d6
33b8a4
0758a5

Requirements
Must have
• Simple easy layout
• Page by page link
• Easy to navigate
• Professional and Welcoming

```html
<!DOCTYPE html>
<html lang="en">
<head>
<meta charset="utf-8">
<title>Whole Heart Living – Psychology &amp; Counselling Relationship Centre</title>
<link href="https://fonts.googleapis.com/css2?family=Carlito:wght@400;700&family=Fira+Sans:wght@300;400;500;600;700&family=Josefin+Sans:wght@600;700&display=swap" rel="stylesheet">
<style>
:root{
  --blue:#32a6d6;
  --button:#2b8fd3;
  --teal:#33b8a4;
  --navy:#0758a5;
  --ink:#1c1c1c;
  --text:#3a3a3a;
  --soft:#f4f0f0;
  --dark:#262626;
  --footer-text:#c9c9c9;
  --white:#ffffff;
}
*{box-sizing:border-box;margin:0;padding:0}
html,body{width:1200px;height:3054px;overflow:hidden}
body{position:relative;background:var(--white);font-family:"Fira Sans",Arial,sans-serif;color:var(--text)}
.abs{position:absolute}

/* header */
.brand{left:132px;top:58px;width:260px}
.brand-row{display:flex;align-items:center;gap:10px}
.brand-dot{width:34px;height:34px;border-radius:50%;background:var(--teal);flex:none}
.brand-name{font-weight:700;font-size:22px;color:var(--navy);letter-spacing:.2px;line-height:1}
.brand-sub{font-size:10.5px;font-weight:500;color:#6b6b6b;margin-top:8px;letter-spacing:.2px}
.contact-item{display:flex;align-items:center;gap:14px}
.contact-icon{width:38px;height:38px;border-radius:50%;background:var(--teal);display:flex;align-items:center;justify-content:center}
.contact-label{font-size:14px;color:var(--ink)}
.contact-value{font-size:18px;font-weight:500;color:var(--navy);margin-top:2px}
.contact-value.phone{font-size:23px;font-weight:600}
.email{left:497px;top:30px}
.call{left:859px;top:30px}
.nav{left:420px;top:104px;display:flex;align-items:stretch}
.nav a{display:flex;align-items:center;font-size:14.5px;color:var(--ink);text-decoration:none;text-transform:uppercase;line-height:18px;padding:0 20px;border-left:1px solid #d8d8d8;height:42px}
.nav a:first-child{border-left:none;padding-left:10px}

/* hero */
.hero{left:0;top:160px;width:1200px;height:562px;background:linear-gradient(100deg,#b9875a 0%,#d8a567 30%,#f4c98a 55%,#c98c55 75%,#7f5a3c 100%)}
.hero-curve{left:0;top:150px}
.hero-title{left:735px;top:425px;font-family:"Josefin Sans",sans-serif;font-weight:700;font-size:50px;color:var(--white);letter-spacing:1px}
.btn{display:inline-block;background:var(--button);color:var(--white);font-weight:600;text-transform:uppercase;text-decoration:none}
.hero-btn{left:739px;top:497px;width:136px;height:43px;line-height:43px;text-align:center;font-size:17px}
.dots{left:558px;top:671px;display:flex;gap:13px;align-items:center}
.dot{width:11px;height:11px;border-radius:50%;background:var(--white)}
.dot.active{width:14px;height:14px;background:var(--navy);border:3px solid var(--white)}

/* sections */
.section-title{font-family:"Josefin Sans",sans-serif;font-weight:700;font-size:33px;color:var(--ink);letter-spacing:1px}
.rule{width:68px;height:4px;background:var(--teal)}
.copy p{font-family:"Carlito",Calibri,sans-serif;font-size:17px;line-height:21.6px;color:var(--text);margin-bottom:21.6px}
.copy.justify p{text-align:justify}
.copy a{color:var(--navy);font-weight:700;text-decoration:none}

.help-image{left:133px;top:776px;width:434px;height:366px;background:linear-gradient(135deg,#3c8fbf 0%,#3fb3a5 100%)}
.help-title{left:619px;top:770px}
.help-rule{left:619px;top:810px}
.help-copy{left:619px;top:850px;width:455px}

.expect-bg{left:0;top:1200px;width:1200px;height:1320px;background:var(--soft)}
.expect-title{left:133px;top:1262px}
.expect-rule{left:133px;top:1304px}
.expect-copy{left:132px;top:1343px;width:418px}
.expect-image{left:606px;top:1264px;width:465px;height:625px;background:linear-gradient(160deg,#e8e6e3 0%,#c9c4bf 45%,#9a8f86 70%,#d9d6d2 100%)}

/* service cards */
.card{top:1948px;width:225px;height:449px;background:var(--white)}
.card-img{width:225px;height:186px}
.card-body{padding:22px 25px 0}
.card-title{font-weight:600;font-size:14.5px;color:var(--ink);text-transform:uppercase;letter-spacing:.4px}
.card-text{font-family:"Carlito",Calibri,sans-serif;font-size:13.5px;line-height:17.6px;color:var(--text);margin-top:12px;height:150px}
.card-btn{width:105px;height:29px;line-height:29px;text-align:center;font-size:12px;letter-spacing:.3px}

/* footer */
.footer{left:0;top:2448px;width:1200px;height:606px}
.footer-brand{left:0;top:2650px;width:1200px;text-align:center}
.footer-brand .brand-row{justify-content:center}
.footer-brand .brand-name{font-size:32px}
.footer-brand .brand-dot{width:44px;height:44px}
.footer-brand .brand-sub{font-size:15px;color:#8a8a8a;margin-top:10px}
.f-contact{display:flex;align-items:center;gap:14px;color:var(--white)}
.f-contact .contact-icon{background:var(--button);width:33px;height:33px}
.f-label{font-size:13px;color:#9a9a9a}
.f-value{font-size:18px;color:var(--white)}
.f-mobile{left:412px;top:2782px}
.f-phone{left:619px;top:2782px}
.f-line{left:256px;width:690px;height:1px;background:#4a4a4a}
.f-nav{left:256px;top:2866px;width:690px;display:flex;justify-content:center}
.f-nav a{font-size:13.5px;color:var(--footer-text);text-decoration:none;padding:0 11px;border-left:1px solid #777;line-height:14px}
.f-nav a:first-child{border-left:none}
.f-about{left:250px;top:2934px;width:700px;text-align:center;font-size:12px;line-height:19px;color:var(--footer-text)}
.f-copy{left:0;top:3011px;width:1200px;text-align:center;font-size:12px;color:var(--footer-text)}
</style>
</head>
<body>

<header>
  <div class="abs brand">
    <div class="brand-row"><span class="brand-dot"></span><span class="brand-name">WHOLE HEART LIVING</span></div>
    <div class="brand-sub">PSYCHOLOGY &amp; COUNSELLING RELATIONSHIP CENTRE</div>
  </div>

  <div class="abs contact-item email">
    <span class="contact-icon"><svg width="16" height="12" viewBox="0 0 16 12"><rect x="0" y="0" width="16" height="12" rx="1.5" fill="#fff"/><path d="M1 1 L8 7 L15 1" stroke="#33b8a4" stroke-width="1.6" fill="none"/></svg></span>
    <div><div class="contact-label">E MAIL US</div><div class="contact-value">info@wholeheartliving.com.au</div></div>
  </div>
  <div class="abs contact-item call">
    <span class="contact-icon"><svg width="16" height="16" viewBox="0 0 24 24"><path fill="#fff" d="M6.6 10.8c1.4 2.8 3.8 5.1 6.6 6.6l2.2-2.2c.3-.3.7-.4 1-.2 1.1.4 2.3.6 3.6.6.6 0 1 .4 1 1V20c0 .6-.4 1-1 1C10.6 21 3 13.4 3 4c0-.6.4-1 1-1h3.5c.6 0 1 .4 1 1 0 1.3.2 2.5.6 3.6.1.3 0 .7-.2 1z"/></svg></span>
    <div><div class="contact-label">CALL US NOW</div><div class="contact-value phone">(02) 9000 1234</div></div>
  </div>

  <nav class="abs nav">
    <a href="#">How we<br>can help</a>
    <a href="#">Relationship<br>counselling</a>
    <a href="#">Parenting</a>
    <a href="#">Courses</a>
    <a href="#">Our team</a>
    <a href="#">Contact</a>
  </nav>
</header>

<section>
  <div class="abs hero" role="img" aria-label="Photo of a man with arms outstretched on a mountain at sunrise"></div>
  <svg class="abs hero-curve" width="1200" height="120" viewBox="0 0 1200 120" aria-hidden="true">
    <path d="M0 0 H1200 V52 Q860 -20 600 88 Q340 -20 0 74 Z" fill="#fff"/>
  </svg>
  <h1 class="abs hero-title">MEN'S ISSUES</h1>
  <a class="abs btn hero-btn" href="#">Read more</a>
  <div class="abs dots"><span class="dot"></span><span class="dot"></span><span class="dot active"></span><span class="dot"></span></div>
</section>

<section>
  <div class="abs help-image" role="img" aria-label="Colour-tinted photo of a smiling couple"></div>
  <h2 class="abs section-title help-title">WHO WE HELP</h2>
  <div class="abs rule help-rule"></div>
  <div class="abs copy help-copy">
    <p>Whole Heart Living Psychology and Counselling Relationship Centre is a team of highly trained professionals provide the ultimate in wellbeing treatment for children, teenagers, adults, parents and couples. We have a strong reputation for providing a warm and personalised service using research based approaches.</p>
    <p>We are passionate and dedicated to helping you get what you want out of life, and we provide life changing treatment for many people, including those experiencing issues such as anxiety, stress, relationship problems. We specialise in Perinatal Anxiety, Parenting and Child issues, Couple Relationship and Men’s issues.</p>
  </div>
</section>

<section>
  <div class="abs expect-bg"></div>
  <h2 class="abs section-title expect-title">WHAT TO EXPECT</h2>
  <div class="abs rule expect-rule"></div>
  <div class="abs copy justify expect-copy">
    <p>Sometimes people don’t know what to expect from the counselling processes. You may wonder if your issues are too complicated, or not serious enough, or worry that the things you’ll discuss will be so distressing that you’ll carry the pain around with you, long after leaving the session.</p>
    <p>What people may not realise is that good therapy can be a joyful experience, despite the need to discuss stressful, sad or shameful things. There’s a beauty in developing insight and making choices from a place of awareness rather than habit or fear.</p>
    <p>There have been lots of tears in our office, it’s true,but there have been even more “Aha!” moments when someone makes a connection between an old belief and a current behaviour. There’ve been quite a few laughs, and exhilarating moments when someone realises they’ve achieved real change.</p>
    <p style="text-align:left">If this resonates with you and you would like personalised support in your relationship, your parenting or just your life in general, <a href="#">please contact us by email or phone.</a></p>
    <p style="text-align:left">We look forward to helping you take that important first step to looking after yourself</p>
  </div>
  <div class="abs expect-image" role="img" aria-label="Photo of a couple talking with a counsellor taking notes"></div>
</section>

<section>
  <article class="abs card" style="left:131px">
    <div class="card-img" role="img" aria-label="Photo of a happy couple in sunlight" style="background:linear-gradient(135deg,#f7e6b8,#e8c08a 60%,#b98b62)"></div>
    <div class="card-body">
      <h3 class="card-title">Couples</h3>
      <p class="card-text">Treatment for couples over 18 years old. We work with married couples, people in life partnerships and same sex couples and provide counselling services to improve the quality of relationships.</p>
      <a class="btn card-btn" href="#">View service</a>
    </div>
  </article>
  <article class="abs card" style="left:370px">
    <div class="card-img" role="img" aria-label="Photo of a parent and child walking on a jetty" style="background:linear-gradient(180deg,#cfd6dc,#9aa4ad 55%,#4f5961)"></div>
    <div class="card-body">
      <h3 class="card-title">Parenting</h3>
      <p class="card-text">We work with parents to improve the quality of relationships between parent and child. We also work with new parents and parents who maybe suffering with post or peri natal depression.</p>
      <a class="btn card-btn" href="#">View service</a>
    </div>
  </article>
  <article class="abs card" style="left:608px">
    <div class="card-img" role="img" aria-label="Photo of two friends blowing glitter" style="background:linear-gradient(135deg,#e7d7e6,#8fa3c2 50%,#3c4f73)"></div>
    <div class="card-body">
      <h3 class="card-title">Adults</h3>
      <p class="card-text">Treatment for individuals over 18 years old. We work with men and women and treat a wide range of mental health issues.</p>
      <a class="btn card-btn" href="#">View service</a>
    </div>
  </article>
  <article class="abs card" style="left:846px">
    <div class="card-img" role="img" aria-label="Photo of children playing with a toy plane on a beach" style="background:linear-gradient(180deg,#eef1f3,#c9d3d8 50%,#8c8a80)"></div>
    <div class="card-body">
      <h3 class="card-title">Children &amp; Teenagers</h3>
      <p class="card-text">Treatment for individuals up to 18 year olds. We work with boys, girls, young adults and their parents and treat a wide range of mental health issues.</p>
      <a class="btn card-btn" href="#">View service</a>
    </div>
  </article>
</section>

<footer>
  <svg class="abs footer" width="1200" height="606" viewBox="0 0 1200 606" aria-hidden="true">
    <path d="M0 56 Q340 -40 600 78 Q860 -40 1200 56 V606 H0 Z" fill="#262626"/>
  </svg>
  <div class="abs footer-brand">
    <div class="brand-row"><span class="brand-dot"></span><span class="brand-name">WHOLE HEART LIVING</span></div>
    <div class="brand-sub">PSYCHOLOGY &amp; COUNSELLING RELATIONSHIP CENTRE</div>
  </div>
  <div class="abs f-contact f-mobile">
    <span class="contact-icon"><svg width="10" height="15" viewBox="0 0 10 15"><rect x="0.8" y="0.8" width="8.4" height="13.4" rx="1.5" fill="none" stroke="#fff" stroke-width="1.6"/><circle cx="5" cy="11.5" r="1" fill="#fff"/></svg></span>
    <div><div class="f-label">Mobile</div><div class="f-value">0400 111 222</div></div>
  </div>
  <div class="abs f-contact f-phone">
    <span class="contact-icon"><svg width="15" height="15" viewBox="0 0 24 24"><path fill="#fff" d="M6.6 10.8c1.4 2.8 3.8 5.1 6.6 6.6l2.2-2.2c.3-.3.7-.4 1-.2 1.1.4 2.3.6 3.6.6.6 0 1 .4 1 1V20c0 .6-.4 1-1 1C10.6 21 3 13.4 3 4c0-.6.4-1 1-1h3.5c.6 0 1 .4 1 1 0 1.3.2 2.5.6 3.6.1.3 0 .7-.2 1z"/></svg></span>
    <div><div class="f-label">Phone</div><div class="f-value">(02) 9000 1234</div></div>
  </div>
  <div class="abs f-line" style="top:2842px"></div>
  <nav class="abs f-nav">
    <a href="#">How We Can Help</a>
    <a href="#">Relationship Counselling</a>
    <a href="#">Parenting</a>
    <a href="#">Courses</a>
    <a href="#">Our Team</a>
    <a href="#">Contact</a>
  </nav>
  <div class="abs f-line" style="top:2904px"></div>
  <p class="abs f-about">Whole Heart Living Psychology and Counselling Relationship Centre is a team of highly trained professionals providing the ultimate in wellbeing treatment for Relationships: couple, parent and baby, child and parent, men isolated from feelings.</p>
  <p class="abs f-copy">Copyright © 2019 All Rights Reserved</p>
</footer>

</body>
</html>
```